Brand Identity Poster - Sabor Ventana

We have a restaurant in Singapore - and looking for a graphic design on a poster - which we can use for all event signage. Our intent is to use this graphic design as a branding mechanism - that whenever the customer sees the image - they know it is Sabor Ventana.

The first photo below is one we found - that we love the combination of the feeling of the poster and the colors. Something similar to this is what we want.

The second file is our new logo.

The third and fourth files show pictures of the restaurant.

The image we wish to convey is relaxed dining - comfortable - and festive. We host a lot of events in the restaurant and we want to be the go-to place for families. We can handle up to 100 people in our restaurant - including outdoor space. Therefore many families and companies hold their gathering here.

Our food is fresh, cooked from the heart and is Filipino and Spanish Fusion. This cuisine includes a lot of seafood and pork.

We offer a great selection of tapas, wine and beer. As we are located in a Business Park, we will also use the image to announce our various "after work" specials so people can relax after hours - before going home.

In our logo - we are not entirely happy with the yellowish colors on the right side. If you have a different yellowish color that works well with the poster - then we are open to modifying the colors in the logo to better match the poster.

The last file is the AI file for the logo - in case you want to modify the colors.

We will make our decision quickly - hence this is a 5 day project.

Good luck and we look forward to your wonderful design ideas.

Project Deadline Extended Reason: Give designers time to adjust their designs based on the feedback given. Added Thursday, June 2, 2016

Hi Designers - we've been very busy in the last 2 days with the final construction of the relaunch. Posting new pictures of the decor, so you can do final design and color tweaks to match. Many thanks for all your great ideas. Added Wednesday, June 8, 2016

Target Market(s)

25 - 40 - Professionals (for professionals during lunch as this is a business park) and Families (for events on evenings and week-ends).

Industry/Entity Type

Restaurant

Requirements
Must have
• Must incorporate our logo - again open to changes in color of the logo - if that works better for you.
• Needs to match our "ventana" name.
• Works well with tapas and wine crowd.
• Have a clearly defined space on the poster - where we can announce different events, as this design will be reused on all events we host.
Nice to have
• The font should be complementary to the font in our logo name. Does not have to be identical - but looks well with the name.
Should not have
• Should not be child-like - as that is too specific of a market.

```html
<!DOCTYPE html>
<html lang="en">
<head>
<meta charset="utf-8">
<title>Sabor Ventana – Event Poster</title>
<link rel="stylesheet" href="https://fonts.googleapis.com/css2?family=Federo&display=swap">
<style>
  :root {
    --sky: #5fb4ea;
    --ocean: #4a70cf;
    --paper: #ffffff;
    --mist: #ececea;
    --tangerine: #f4733a;
    --sun: #fbe54e;
    --lagoon: #3aaba3;
    --leaf-blue: #6cbcef;
    --brand-orange: #f26a2e;
    --brand-blue: #3f6fcf;
  }
  * { margin: 0; padding: 0; box-sizing: border-box; }
  html, body {
    width: 839px;
    height: 1200px;
    overflow: hidden;
    background: var(--mist);
  }
  .poster {
    position: relative;
    width: 839px;
    height: 1200px;
    overflow: hidden;
    background: var(--sky);
  }
  .poster__art {
    position: absolute;
    inset: 0;
    width: 839px;
    height: 1200px;
  }
  .event-panel {
    position: absolute;
    left: 166px;
    top: 124px;
    width: 506px;
    height: 877px;
    background: var(--paper);
  }
  .brand {
    position: absolute;
    left: 166px;
    top: 292px;
    width: 506px;
    text-align: center;
    font-family: "Federo", sans-serif;
  }
  .brand__name {
    font-size: 38px;
    letter-spacing: 1px;
    color: var(--brand-orange);
    line-height: 1;
  }
  .brand__dot {
    display: block;
    width: 18px;
    height: 18px;
    margin: 0 auto 14px;
    border-radius: 50%;
    background: var(--brand-orange);
  }
  .brand__tagline {
    margin-top: 10px;
    font-size: 11px;
    letter-spacing: 1.5px;
    text-transform: uppercase;
    color: var(--brand-blue);
  }
</style>
</head>
<body>
<main class="poster">
  <svg class="poster__art" viewBox="0 0 839 1200" xmlns="http://www.w3.org/2000/svg">
    <defs>
      <linearGradient id="flowerTone" x1="0" y1="0" x2="1" y2="1">
        <stop offset="0" stop-color="#f4733a"/>
        <stop offset="1" stop-color="#f58a55"/>
      </linearGradient>
      <linearGradient id="monsteraTone" x1="0" y1="0" x2="1" y2="1">
        <stop offset="0" stop-color="#3aaba3"/>
        <stop offset="1" stop-color="#2f9b94"/>
      </linearGradient>
      <linearGradient id="fernTone" x1="0" y1="0" x2="0" y2="1">
        <stop offset="0" stop-color="#6cbcef"/>
        <stop offset="1" stop-color="#3aaba3"/>
      </linearGradient>
    </defs>

    <!-- frame band -->
    <rect class="frame-band" x="93" y="118" width="667" height="960" fill="var(--ocean)"/>
    <rect class="mist-patch" x="0" y="0" width="839" height="120" fill="var(--mist)"/>

    <!-- foliage zones -->
    <g role="img" aria-label="Orange tropical flower and leaves in the top left corner">
      <path d="M0 0 H260 C250 120 200 230 110 300 C60 330 20 320 0 310 Z" fill="url(#flowerTone)"/>
    </g>
    <g role="img" aria-label="Light blue palm fronds along the top edge">
      <path d="M240 0 H560 C520 70 440 110 340 120 C300 100 260 60 240 0 Z" fill="var(--leaf-blue)"/>
    </g>
    <g role="img" aria-label="Teal monstera leaf in the top right corner">
      <path d="M500 90 C560 10 760 -10 839 20 V240 C760 280 620 270 540 220 C500 190 480 140 500 90 Z" fill="url(#monsteraTone)"/>
    </g>
    <g role="img" aria-label="Yellow palm leaf reaching in from the right edge">
      <path d="M839 230 V470 C760 490 660 460 620 400 C660 330 760 260 839 230 Z" fill="var(--sun)"/>
    </g>
    <g role="img" aria-label="Teal fronds along the left edge">
      <path d="M0 300 C60 320 130 380 160 440 C120 470 50 470 0 450 Z" fill="var(--lagoon)"/>
    </g>
    <g role="img" aria-label="Yellow palm leaf and orange seed pods on the left edge">
      <path d="M0 450 C70 470 140 560 160 680 C120 760 60 790 0 800 Z" fill="var(--sun)"/>
    </g>
    <g role="img" aria-label="Two guests chatting at a high table on the right">
      <path d="M672 490 H760 V680 H672 Z" fill="var(--leaf-blue)"/>
    </g>
    <g role="img" aria-label="Light blue leaf with yellow dots on the lower right">
      <path d="M672 690 C740 700 839 740 839 780 V1060 C780 1070 700 1040 672 1000 Z" fill="var(--leaf-blue)"/>
    </g>
    <g role="img" aria-label="Teal fern and orange berries along the bottom">
      <path d="M260 1200 C300 1060 400 960 520 900 C600 940 660 1060 680 1200 Z" fill="url(#fernTone)"/>
    </g>
    <g role="img" aria-label="Couple seated at a round café table in the bottom left">
      <path d="M0 1000 C60 960 180 950 240 1000 C260 1080 220 1160 160 1200 H0 Z" fill="var(--leaf-blue)"/>
    </g>
    <g role="img" aria-label="Pale leaf at the bottom right corner">
      <path d="M620 1200 C680 1130 780 1100 839 1110 V1200 Z" fill="var(--mist)"/>
    </g>
  </svg>

  <section class="event-panel" aria-label="Event announcement space"></section>

  <header class="brand">
    <span class="brand__dot" aria-hidden="true"></span>
    <h1 class="brand__name">Sabor Ventana</h1>
    <p class="brand__tagline">Spanish Filipino Fusion</p>
  </header>
</main>
</body>
</html>
```